Chinese Herbal and Roots Shop design

Hello Designers,

We are a herbal startup company which sells Chinese Herbal Products. we are looking for a responsive and unqiue Ecommerce web design.
Our business name is velorin and our area of business cut across the entire United States.

We don't have a logo at the moment and designers who come up with a great logo is more likely to be awarded winner of the consent.

The design needs to be completely custom design and we are not after just a template design. Please be creative and at the same time design have to be professionally looking and easy to navigate.
A theme which suits a herbal products are desired. We are open to different colors excpet RED and PINK.

NAVIGATION
Header -
Home, products, offers, Blog, cart, login/account

Footer -
Please refer to other Ecommerce websites

Page requires:
HOME PAGE
1. slider(Highlist products)
2. FEATURE PRODUCTS
3. Latest products
4. Most selling products
5. Deal of the day
6. Email capture (Newsletter/signup)
7. Social media links
8. Footer

PRODUCT PAGE
All the products will be present here with required details (price, short note and offers if any)

PRODUCT DETAILS PAGE
A well designed detailed page for a particular product covers the details of the price, increment, short description, purchase and other add to cart button. A section with similar products should be listed below aswell.

Industry/Entity Type

It Company

Coding

Coded - Design and coding required

```html
<!DOCTYPE html>
<html lang="en">
<head>
<meta charset="utf-8">
<title>velorin — Natural Herbal Health Products</title>
<link href="https://fonts.googleapis.com/css2?family=Open+Sans:wght@400;600;700&family=Raleway:wght@400;500;600&display=swap" rel="stylesheet">
<style>
:root{
  --green:#7cb82f;
  --green-dark:#5e9a1c;
  --green-deep:#3f6a26;
  --green-light:#c9e39d;
  --ink:#333;
  --muted:#8a8a8a;
  --line:#e3e3e3;
  --paper:#ffffff;
  --footer:#1d1d1d;
  --footer-2:#141414;
  --price:#6a9d26;
}
*{box-sizing:border-box;margin:0;padding:0}
html,body{width:1200px;height:3048px;overflow:hidden}
body{font-family:"Open Sans",Arial,sans-serif;color:var(--ink);background:var(--paper);position:relative}
.wrap{width:800px;margin:0 auto;position:relative}
.section-title{font-family:"Raleway",Arial,sans-serif;font-weight:500;font-size:28px;line-height:34px;text-align:center;color:#333}

/* header */
.site-header{height:80px;position:relative;background:var(--paper)}
.search{position:absolute;left:216px;top:18px;width:110px;height:20px;border:1px solid var(--line);border-radius:2px;background:#fafafa}
.brand{position:absolute;left:50%;top:12px;transform:translateX(-50%);text-align:center}
.brand-mark{display:block;width:18px;height:18px;border-radius:50%;background:var(--green);margin:0 auto 3px}
.brand-name{font-family:"Raleway",Arial,sans-serif;font-weight:600;font-size:26px;color:var(--green);line-height:1}
.nav{position:absolute;top:58px;font-size:12px;line-height:14px;display:flex;gap:26px}
.nav a{color:#555;text-decoration:none}
.nav a.active{color:var(--green);font-weight:600}
.nav-left{left:352px}
.nav-right{left:690px}
.account{position:absolute;right:200px;top:14px;display:flex;align-items:center;gap:10px;font-size:11px;color:#666}
.btn-login{background:var(--green);color:#fff;padding:4px 14px;border-radius:2px;font-size:11px}

/* hero */
.hero{height:380px;position:relative;background:linear-gradient(180deg,#f6f6f6 0%,#ececec 60%,#e4e4e4 100%);overflow:hidden}
.hero-curve{position:absolute;left:0;top:0}
.hero-text{position:absolute;left:216px;top:80px;width:290px;color:#fff}
.hero-tag{display:inline-block;background:var(--green-dark);font-size:14px;padding:6px 12px;font-weight:600}
.hero-text p{font-size:10px;line-height:1.5;margin-top:10px;color:#f1f8e6}
.hero-photo{position:absolute;left:560px;top:16px;width:460px;height:260px;border-radius:8px;background:radial-gradient(ellipse at 45% 50%,#ffffff 0%,#f1f1ea 45%,#c9c2ad 80%,#dcdcd4 100%)}
.perks{position:absolute;left:216px;top:330px;display:flex;gap:46px;color:#fff;font-size:13px}
.perk{display:flex;align-items:center;gap:10px;line-height:1.15}
.perk svg{flex:none}

/* feature products */
.feature{padding-top:44px;height:760px}
.tabs{display:flex;justify-content:center;gap:8px;margin-top:16px;font-size:9px;color:#777}
.tabs span{padding:2px 6px;border:1px solid transparent}
.tabs span.on{border-color:#ccc;color:#333}
.grid{display:grid;grid-template-columns:repeat(4,182px);column-gap:24px;row-gap:30px;margin-top:28px}
.card{border:1px solid var(--line);background:var(--paper);height:270px;position:relative}
.card-img{height:190px;margin:10px;background:linear-gradient(180deg,#fff,#f1f1f1)}
.card-img.red{background:radial-gradient(ellipse at 50% 50%,#d43b3b 0%,#b72222 22%,#ffffff 24%,#ffffff 100%)}
.card-img.jar{background:radial-gradient(ellipse at 50% 55%,#4a2d20 0%,#3a2218 20%,#ffffff 22%)}
.card-img.tub{background:radial-gradient(ellipse at 50% 60%,#e8eef2 0%,#c9d3da 26%,#ffffff 28%)}
.card-name{font-size:9px;line-height:12px;color:#555;margin:0 10px}
.card-foot{display:flex;justify-content:space-between;align-items:center;margin:10px 10px 0}
.btn-cart{background:var(--green);color:#fff;font-size:11px;line-height:14px;padding:5px 12px;border-radius:2px}
.price{font-size:13px;color:#444}

/* latest */
.latest{height:380px;position:relative;background:linear-gradient(90deg,#dff0c4 0%,#f7fbf0 25%,#ffffff 50%,#f7fbf0 75%,#d6ecb5 100%);padding-top:40px}
.latest-row{display:flex;gap:16px;margin-top:30px}
.l-card{width:188px;background:var(--paper);border:1px solid var(--line);padding:10px;height:220px;position:relative}
.l-img{height:160px}
.l-card .card-name{margin:12px 0 0}
.l-badge{position:absolute;left:10px;top:140px;background:var(--green);color:#fff;font-size:11px;padding:3px 8px}
.l-more{position:absolute;left:150px;top:138px;width:22px;height:22px;border-radius:50%;background:#fff;border:2px solid var(--green)}

/* most selling */
.selling{height:360px;padding-top:26px}
.sell-row{display:flex;gap:16px;margin-top:20px}
.s-card{width:188px;border:1px solid var(--line);padding:10px;height:262px}
.s-img{height:180px}
.s-meta{display:flex;justify-content:space-between;align-items:center;margin-top:8px;height:22px}
.s-meta small{font-size:8px;color:#666;line-height:1.3;width:96px}
.s-meta b{font-size:15px;color:var(--price);font-weight:600}
.s-card .btn-cart{display:block;text-align:center;margin-top:8px}

/* deal of the day */
.deals{display:flex;height:440px}
.deal{width:400px;height:440px;position:relative;overflow:hidden}
.deal-img{position:absolute;inset:0}
.deal-copy{position:absolute;left:0;right:0;bottom:0;height:180px;padding:22px 24px;color:#fff;background:var(--green)}
.deal h3{font-family:"Raleway",Arial,sans-serif;font-weight:600;font-size:22px;line-height:1.15;width:210px}
.deal .amount{position:absolute;right:24px;top:64px;font-size:24px;font-weight:600}
.deal p{font-size:9px;line-height:1.4;margin-top:8px;width:170px}
.deal .btn-cart{position:absolute;left:24px;bottom:22px;background:#fff;color:var(--green-dark)}
.deal-2 .deal-img{background:linear-gradient(90deg,#24361a 0%,#3f5a2a 45%,#e9f3dc 52%,#f6faef 100%)}
.deal-2 .deal-copy{left:210px;top:40px;height:auto;background:none;color:var(--green-deep);padding:0}
.deal-2 h3{font-size:38px;line-height:1;width:170px;font-weight:500}
.deal-2 p{color:#555;width:160px}
.deal-2 .amount{position:static;display:block;margin-top:120px;font-size:24px;color:#333}
.deal-2 .btn-cart{position:static;display:inline-block;margin-top:14px;background:var(--green);color:#fff}
.deal-3 .deal-img{background:linear-gradient(90deg,#fff 0%,#fff 45%,#dfeecb 100%)}
.deal-3 .deal-copy{height:230px}
.deal-3 h3{font-size:24px;width:230px}
.deal-3 .amount{top:150px}

/* newsletter */
.newsletter{height:360px;position:relative;background:radial-gradient(ellipse at 50% 55%,#fafdf4 0%,#e8f4d6 45%,#b7db80 80%,#8fc24b 100%);text-align:center;padding-top:54px}
.mail-ico{display:block;margin:0 auto}
.newsletter h2{font-family:"Raleway",Arial,sans-serif;font-weight:500;font-size:32px;color:#333;margin-top:14px}
.fields{display:flex;justify-content:center;gap:20px;margin-top:30px}
.fields span{width:220px;height:30px;background:#fff;border:1px solid #ddd;text-align:left;padding:7px 10px;font-size:11px;color:#aaa}
.btn-signup{display:inline-block;margin-top:22px;background:var(--green);color:#fff;font-size:14px;padding:8px 44px;border-radius:2px}

/* footer */
.site-footer{height:288px;background:var(--footer);color:#bbb;position:relative}
.follow{height:40px;background:var(--footer-2);display:flex;justify-content:center;align-items:center;gap:10px;font-size:11px;color:#ddd}
.follow i{width:12px;height:12px;border-radius:50%;background:#ddd;display:block}
.footer-cols{display:flex;gap:40px;margin-top:28px}
.col{width:170px;font-size:10px;line-height:1.9}
.col h4{color:var(--green);font-size:12px;font-weight:600;margin-bottom:6px}
.col.news{width:230px}
.col.news p{line-height:1.5;margin-bottom:10px}
.col.news p b{display:block;color:var(--green);font-weight:400}
</style>
</head>
<body>

<header class="site-header">
  <span class="search"></span>
  <nav class="nav nav-left"><a class="active">Home</a><a>Products</a><a>Offers</a></nav>
  <div class="brand"><span class="brand-mark"></span><span class="brand-name">velorin</span></div>
  <nav class="nav nav-right"><a>Blog</a><a>Cart</a><a>Contact</a></nav>
  <div class="account">
    <svg width="14" height="12" viewBox="0 0 14 12"><path d="M0 1h3l2 7h7l2-5H4" fill="none" stroke="#666" stroke-width="1.3"/><circle cx="6" cy="10.5" r="1.2" fill="#666"/><circle cx="11" cy="10.5" r="1.2" fill="#666"/></svg>
    <span>0 item</span><span class="btn-login">Login</span>
  </div>
</header>

<section class="hero">
  <svg class="hero-curve" width="1200" height="380" viewBox="0 0 1200 380">
    <path d="M0 40 C 250 50, 420 40, 560 70 L 560 250 C 420 240, 250 270, 0 250 Z" fill="#8cc63f"/>
    <path d="M0 280 C 300 240, 600 300, 900 270 C 1050 255, 1150 270, 1200 275 L1200 380 L0 380 Z" fill="#7cb82f"/>
    <path d="M0 270 C 300 230, 600 290, 900 258 C 1050 244, 1150 258, 1200 262 L1200 280 C 1150 275, 1050 262, 900 276 C 600 306, 300 246, 0 288 Z" fill="#c9e39d"/>
  </svg>
  <div class="hero-photo" role="img" aria-label="White herbal supplement bottles with a mortar of dried roots and green leaves"></div>
  <div class="hero-text">
    <span class="hero-tag">All Natural Herbal Health Products</span>
    <p>Traditional herbs and roots gathered with care, tested for purity and packed fresh so every blend keeps its natural strength for your daily wellness.</p>
  </div>
  <div class="perks">
    <div class="perk"><svg width="26" height="26" viewBox="0 0 26 26"><rect x="7" y="2" width="12" height="22" rx="2" fill="none" stroke="#fff" stroke-width="2"/><circle cx="13" cy="20" r="1.3" fill="#fff"/></svg>Phone<br>Support</div>
    <div class="perk"><svg width="26" height="26" viewBox="0 0 26 26"><circle cx="13" cy="13" r="11" fill="none" stroke="#fff" stroke-width="2"/><path d="M8 13l4 4 7-8" fill="none" stroke="#fff" stroke-width="2"/></svg>Money<br>Guarantee</div>
    <div class="perk"><svg width="30" height="26" viewBox="0 0 30 26"><rect x="1" y="6" width="17" height="12" fill="none" stroke="#fff" stroke-width="2"/><path d="M18 10h6l4 4v4H18z" fill="none" stroke="#fff" stroke-width="2"/><circle cx="7" cy="21" r="2.5" fill="#fff"/><circle cx="23" cy="21" r="2.5" fill="#fff"/></svg>Free<br>Shipping</div>
  </div>
</section>

<section class="feature">
  <h2 class="section-title">Feature Products</h2>
  <div class="tabs"><span class="on">All</span><span>Weight Gain</span><span>Herbal Formulas</span><span>Liquid Herbs</span><span>Herbal Teas</span><span>Roots Herbs</span><span>Specialty Herbs</span></div>
  <div class="wrap grid">
    <div class="card"><div class="card-img red" role="img" aria-label="Red herbal supplement box"></div><div class="card-name">Jade Root Vital Blend</div><div class="card-foot"><span class="btn-cart">Add to Cart</span><span class="price">$ 169.95</span></div></div>
    <div class="card"><div class="card-img jar" role="img" aria-label="Dark herbal capsule bottle"></div><div class="card-name">Jade Root Vital Blend</div><div class="card-foot"><span class="btn-cart">Add to Cart</span><span class="price">$ 169.95</span></div></div>
    <div class="card"><div class="card-img red" role="img" aria-label="Red herbal supplement box"></div><div class="card-name">Jade Root Vital Blend</div><div class="card-foot"><span class="btn-cart">Add to Cart</span><span class="price">$ 169.95</span></div></div>
    <div class="card"><div class="card-img jar" role="img" aria-label="Dark herbal capsule bottle"></div><div class="card-name">Jade Root Vital Blend</div><div class="card-foot"><span class="btn-cart">Add to Cart</span><span class="price">$ 169.95</span></div></div>
    <div class="card"><div class="card-img jar" role="img" aria-label="White and red supplement bottle"></div><div class="card-name">Jade Root Vital Blend</div><div class="card-foot"><span class="btn-cart">Add to Cart</span><span class="price">$ 169.95</span></div></div>
    <div class="card"><div class="card-img tub" role="img" aria-label="Pair of white supplement tubs"></div><div class="card-name">Jade Root Vital Blend</div><div class="card-foot"><span class="btn-cart">Add to Cart</span><span class="price">$ 169.95</span></div></div>
    <div class="card"><div class="card-img tub" role="img" aria-label="White supplement tub"></div><div class="card-name">Jade Root Vital Blend</div><div class="card-foot"><span class="btn-cart">Add to Cart</span><span class="price">$ 169.95</span></div></div>
    <div class="card"><div class="card-img red" role="img" aria-label="Red herbal supplement box"></div><div class="card-name">Jade Root Vital Blend</div><div class="card-foot"><span class="btn-cart">Add to Cart</span><span class="price">$ 169.95</span></div></div>
  </div>
</section>

<section class="latest" role="img" aria-label="Soft background of fresh green leaves">
  <h2 class="section-title">Latest Products</h2>
  <div class="wrap latest-row">
    <div class="l-card"><div class="l-img" style="background:radial-gradient(ellipse at 50% 55%,#e9eef0 0%,#cfd8dc 30%,#fff 33%)" role="img" aria-label="White supplement bottle"></div><div class="card-name">Gelatinized Maca Organic</div></div>
    <div class="l-card"><div class="l-img" style="background:radial-gradient(ellipse at 50% 50%,#3f5a2a 0%,#2f3f22 28%,#fff 31%)" role="img" aria-label="Dark green capsule bottle"></div><span class="l-badge">$120.00</span><span class="l-more"></span><div class="card-name">Gelatinized Maca Organic</div></div>
    <div class="l-card"><div class="l-img" style="background:radial-gradient(ellipse at 50% 55%,#c98f86 0%,#a8685e 28%,#fff 31%)" role="img" aria-label="Brown powder tub"></div><div class="card-name">Gelatinized Maca Organic</div></div>
    <div class="l-card"><div class="l-img" style="background:radial-gradient(ellipse at 50% 55%,#e7c04a 0%,#3c6fb0 30%,#fff 33%)" role="img" aria-label="Blue and yellow supplement bottle"></div><div class="card-name">Gelatinized Maca Organic</div></div>
  </div>
</section>

<section class="selling">
  <h2 class="section-title">Most Selling Products</h2>
  <div class="wrap sell-row">
    <div class="s-card"><div class="s-img" style="background:radial-gradient(ellipse at 50% 55%,#2f4a22 0%,#24361a 28%,#ececec 31%)" role="img" aria-label="Dark herbal capsule bottle"></div><div class="s-meta"><small>Lotus Root Herbal Pearl</small><b>$29.23</b></div><span class="btn-cart">Add to Cart</span></div>
    <div class="s-card"><div class="s-img" style="background:radial-gradient(ellipse at 50% 55%,#5c8d3a 0%,#3f6a26 30%,#ececec 33%)" role="img" aria-label="Green herbal hair tonic box and bottle"></div><div class="s-meta"><small>Lotus Root Herbal Pearl</small><b>$29.23</b></div><span class="btn-cart">Add to Cart</span></div>
    <div class="s-card"><div class="s-img" style="background:radial-gradient(ellipse at 50% 55%,#fff 0%,#dfe5e8 30%,#ececec 33%)" role="img" aria-label="White supplement bottle"></div><div class="s-meta"><small>Lotus Root Herbal Pearl</small><b>$29.23</b></div><span class="btn-cart">Add to Cart</span></div>
    <div class="s-card"><div class="s-img" style="background:radial-gradient(ellipse at 50% 55%,#d8434b 0%,#f5f5f5 30%,#ececec 33%)" role="img" aria-label="White and red supplement box"></div><div class="s-meta"><small>Lotus Root Herbal Pearl</small><b>$29.23</b></div><span class="btn-cart">Add to Cart</span></div>
  </div>
</section>

<section class="deals">
  <div class="deal deal-1">
    <div class="deal-img" role="img" aria-label="Row of colourful turmeric supplement bottles" style="background:linear-gradient(180deg,#f7f7f5 0%,#ece6dc 60%,#e0d4c2 100%)"></div>
    <div class="deal-copy"><h3>Turmeric Root Fiji Fresh Organic</h3><p>Bright golden root, dried slowly to keep its warm taste.</p><span class="amount">$ 230.00</span><span class="btn-cart">Add to Cart</span></div>
  </div>
  <div class="deal deal-2">
    <div class="deal-img" role="img" aria-label="Dark green hair growth box with bottle"></div>
    <div class="deal-copy"><h3>Hair Growth</h3><p>Gentle herbal care that nourishes roots and supports fuller hair.</p><span class="amount">$ 125.00</span><span class="btn-cart">Add to Cart</span></div>
  </div>
  <div class="deal deal-3">
    <div class="deal-img" role="img" aria-label="Hair tonic bottle and box on white"></div>
    <div class="deal-copy"><h3>Gelatinized Maca Powder Organic</h3><p>Pure root powder, gently processed for easy daily use.</p><span class="amount">$ 351.00</span><span class="btn-cart">Add to Cart</span></div>
  </div>
</section>

<section class="newsletter" role="img" aria-label="Bright background of sunlit green leaves">
  <svg class="mail-ico" width="44" height="44" viewBox="0 0 44 44"><rect x="2" y="2" width="40" height="40" rx="3" fill="none" stroke="#333" stroke-width="2"/><rect x="10" y="14" width="24" height="17" fill="none" stroke="#333" stroke-width="2"/><path d="M10 14l12 10 12-10" fill="none" stroke="#333" stroke-width="2"/></svg>
  <h2>Singup for our Awesome Newsletter</h2>
  <div class="fields"><span>Name</span><span>Email</span></div>
  <span class="btn-signup">Signup</span>
</section>

<footer class="site-footer">
  <div class="follow">Follow us <i></i><i></i><i></i><i></i><i></i></div>
  <div class="wrap footer-cols">
    <div class="col"><h4>Information</h4>Home<br>Products<br>Offers<br>Blog<br>Cart<br>Contact</div>
    <div class="col"><h4>Why buy from us</h4>Shipping &amp; Returns<br>Secure Shopping<br>International Shipping<br>Affiliates<br>Group Sales</div>
    <div class="col"><h4>Information</h4>About Us<br>Privacy Policy<br>My Wishlist<br>Track My Order</div>
    <div class="col news"><h4>News</h4>
      <p><b>New herbal tea range arrives</b>Fresh blends picked this season are now in stock.</p>
      <p><b>Free shipping this month</b>Orders across the country ship free until the end of the month.</p>
    </div>
  </div>
</footer>

</body>
</html>
```